We need a design for our retail display and for our stockist's retail display.
Our product is fresh corn tortillas. These can be used to make tacos, quesadillas, tortilla chips and tostadas.
We want the table talker to use our brand style (see our website) and show the tortillas versatility.
kelvo-flatbreads.co.uk
It should also have a space for our stockists to write in a blank space under the heading "Our fresh tortillas are delivered every....[blank space]"
The table talker should be 75mm tall x 150mm wide. This will also have a 25mm self adhesive flap at the top which can be blank or the same colour as the background.
Please feel free to use any files from our website as well as illustrations attached.
Target Market(s)
Customers in high end shops and delis
Industry/Entity Type
food and drink
Look and feel

```html
<!DOCTYPE html>
<html lang="en">
<head>
<meta charset="utf-8">
<title>Kelvo Flatbreads – Fresh Corn Tortillas Table Talker</title>
<link href="https://fonts.googleapis.com/css2?family=Oswald:wght@500;700&family=Roboto+Condensed:wght@400&display=swap" rel="stylesheet">
<style>
  :root {
    --page-bg: #e8e5e2;
    --brand-yellow: #f7d417;
    --brand-yellow-deep: #ecc90f;
    --brand-navy: #1e2c49;
    --note-cream: #fcfaf0;
    --ink: #161616;
  }
  * { box-sizing: border-box; margin: 0; padding: 0; }
  html, body {
    width: 1200px; height: 1043px; overflow: hidden;
    background: var(--page-bg);
  }
  .table-talker {
    position: absolute; left: 50px; top: 98px;
    width: 1100px; height: 846px;
    background: linear-gradient(180deg, var(--brand-yellow) 0%, var(--brand-yellow-deep) 100%);
    overflow: hidden;
  }
  .headline {
    position: absolute; left: 0; right: 0; top: 218px;
    text-align: center;
    font-family: "Oswald", sans-serif; font-weight: 700;
    font-size: 104px; line-height: 1; letter-spacing: 2px;
    color: var(--brand-navy); text-transform: uppercase;
  }
  .delivery-note {
    position: absolute; left: 82px; right: 78px; top: 352px; height: 146px;
    background: var(--note-cream); border-radius: 14px;
  }
  .delivery-note__text {
    position: absolute; left: 0; right: 0; top: 24px; text-align: center;
    font-family: "Roboto Condensed", sans-serif; font-weight: 400;
    font-size: 36px; color: var(--ink); text-transform: uppercase;
  }
  .delivery-note__blank {
    position: absolute; left: 92px; right: 108px; top: 108px;
    border-top: 1.5px solid var(--ink);
  }
  .claims {
    position: absolute; left: 0; right: 0; top: 520px;
    display: flex; justify-content: center; gap: 40px;
  }
  .claim {
    width: 84px; height: 84px; border-radius: 50%;
    background: var(--brand-navy);
    border: 3px solid var(--brand-navy);
    box-shadow: inset 0 0 0 3px var(--brand-yellow);
    display: flex; flex-direction: column; align-items: center; justify-content: center;
    font-family: "Oswald", sans-serif; font-weight: 500;
    color: var(--brand-yellow); text-transform: uppercase; text-align: center; line-height: 1;
  }
  .claim__big { font-size: 24px; }
  .claim__small { font-size: 10px; margin-top: 2px; }
  .uses-band {
    position: absolute; left: 0; right: 0; top: 610px; bottom: 0;
    background: var(--brand-navy);
  }
  .brand {
    position: absolute; left: 32px; top: 94px;
    display: flex; align-items: center; gap: 10px;
    font-family: "Oswald", sans-serif; font-weight: 500;
    font-size: 24px; color: var(--brand-yellow); text-transform: uppercase;
  }
  .brand__dot { width: 16px; height: 16px; border-radius: 50%; background: var(--brand-yellow); }
  .uses {
    position: absolute; left: 230px; right: 40px; top: 22px;
    display: flex; justify-content: space-between;
  }
  .use { width: 150px; display: flex; flex-direction: column; align-items: center; }
  .use__art {
    width: 130px; height: 128px; border-radius: 18px;
    background: linear-gradient(160deg, #3a4968 0%, #2a3858 100%);
  }
  .use__label {
    margin-top: 20px;
    font-family: "Oswald", sans-serif; font-weight: 500;
    font-size: 22px; color: var(--brand-yellow); text-transform: uppercase; white-space: nowrap;
  }
</style>
</head>
<body>
  <main class="table-talker">
    <h1 class="headline">Fresh Corn Tortillas</h1>

    <section class="delivery-note">
      <p class="delivery-note__text">Our fresh tortillas are delivered every</p>
      <div class="delivery-note__blank"></div>
    </section>

    <ul class="claims" style="list-style:none">
      <li class="claim"><span class="claim__big">No</span><span class="claim__small">Preservatives</span></li>
      <li class="claim"><span class="claim__big">Vegan</span></li>
      <li class="claim"><span class="claim__big">100%</span><span class="claim__small">Biodegradable<br>Recyclable</span></li>
      <li class="claim"><span class="claim__big">No<br>GMO</span></li>
      <li class="claim"><span class="claim__big">Gluten</span><span class="claim__small">Free</span></li>
    </ul>

    <section class="uses-band">
      <div class="brand"><span class="brand__dot"></span>Kelvo Flatbreads</div>
      <div class="uses">
        <div class="use"><div class="use__art" role="img" aria-label="Line illustration of a taco"></div><span class="use__label">Tacos</span></div>
        <div class="use"><div class="use__art" role="img" aria-label="Line illustration of a quesadilla wedge"></div><span class="use__label">Quesadilla</span></div>
        <div class="use"><div class="use__art" role="img" aria-label="Line illustration of a tortilla chip with dip"></div><span class="use__label">Tortilla Chips</span></div>
        <div class="use"><div class="use__art" role="img" aria-label="Line illustration of a taquito"></div><span class="use__label">Taquitos</span></div>
        <div class="use"><div class="use__art" role="img" aria-label="Line illustration of a topped tostada"></div><span class="use__label">Tostada</span></div>
      </div>
    </section>
  </main>
</body>
</html>
```